female esthetician looking for an impact business card

I an an expert in skin care industry with high experience in NYC.I want my business card to look professional , an impact at first look. I do want a combination between white and gold . I believe the font will be great if is gold.. The Fonts are also important. MARISELA VONDRAKE (SKIN CARE BOUTIQUE)

THIS SHOULD BE THE BUSINESS NAME, and should be placed on th eback of the card.
IN front m, the name MARISELA VONDRAKE - ESTHETCIAN

BY APPOINTMENTS ONLY: 555.218.9031

Target Market(s)

HIGH END CLIENTELE

Contact Information for Business Card

iT WILL BE on a luxury paper. I neeed the wow feeling

Requirements
Should not have
• pictures

```html
<!DOCTYPE html>
<html lang="en">
<head>
<meta charset="utf-8">
<title>Marisela Vondrake – Business Card</title>
<link rel="stylesheet" href="https://fonts.googleapis.com/css2?family=Montserrat:wght@600&family=Open+Sans:wght@400&display=swap">
<style>
  :root {
    --stage: #1c1c1c;
    --card-dark: #1d1d1d;
    --card-light: #ffffff;
    --gold-deep: #a87a1c;
    --gold-mid: #d9ad3c;
    --gold-light: #f4dc7a;
    --gold-gradient: linear-gradient(120deg, var(--gold-deep) 0%, var(--gold-light) 45%, var(--gold-mid) 70%, var(--gold-deep) 100%);
  }
  html, body {
    margin: 0;
    width: 1200px;
    height: 895px;
    overflow: hidden;
    background: var(--stage);
  }
  .canvas {
    position: relative;
    width: 1200px;
    height: 895px;
  }
  .card {
    position: absolute;
    top: 128px;
    width: 380px;
    height: 640px;
    box-shadow: 0 18px 40px rgba(0,0,0,0.55);
  }
  .card--dark { left: 180px; background: var(--card-dark); }
  .card--light { left: 640px; background: var(--card-light); }

  .frame {
    position: absolute;
    top: 20px;
    left: 20px;
    width: 340px;
    height: 310px;
    overflow: visible;
  }
  .gold-text {
    background: var(--gold-gradient);
    -webkit-background-clip: text;
    background-clip: text;
    color: transparent;
  }
  .card__title {
    position: absolute;
    top: 136px;
    right: 28px;
    margin: 0;
    font-family: 'Open Sans', sans-serif;
    font-size: 15px;
    line-height: 20px;
    letter-spacing: 0.5px;
  }
  .card__name {
    position: absolute;
    top: 160px;
    left: 38px;
    margin: 0;
    font-family: 'Montserrat', sans-serif;
    font-weight: 600;
    font-size: 25px;
    line-height: 32px;
    letter-spacing: 0.8px;
    white-space: nowrap;
  }
  .contact {
    position: absolute;
    top: 488px;
    left: 40px;
    right: 36px;
    font-family: 'Open Sans', sans-serif;
    text-align: right;
  }
  .contact__row {
    display: flex;
    justify-content: flex-end;
    align-items: center;
    gap: 12px;
  }
  .contact__icons { display: flex; flex-direction: column; gap: 6px; }
  .contact__phone { font-size: 24px; line-height: 32px; letter-spacing: 1px; margin: 0; }
  .contact__email { font-size: 15px; line-height: 20px; margin: 4px 0 0; }
  .contact__web { font-size: 16px; line-height: 22px; margin: 6px 28px 0 0; }
  .contact__rule {
    display: block;
    margin: 16px 28px 0 auto;
    width: 70px;
    height: 2px;
    background: var(--gold-gradient);
  }
</style>
</head>
<body>
<main class="canvas">
  <svg width="0" height="0" style="position:absolute">
    <defs>
      <linearGradient id="goldStroke" x1="0" y1="0" x2="1" y2="1">
        <stop offset="0" stop-color="#a87a1c"/>
        <stop offset="0.45" stop-color="#f4dc7a"/>
        <stop offset="0.7" stop-color="#d9ad3c"/>
        <stop offset="1" stop-color="#a87a1c"/>
      </linearGradient>
    </defs>
  </svg>

  <section class="card card--dark">
    <svg class="frame" viewBox="0 0 340 310" aria-hidden="true">
      <path d="M340,108 V0 H0 V310 H340 V188" fill="none" stroke="url(#goldStroke)" stroke-width="2"/>
    </svg>
    <p class="card__title gold-text">Skin care expert</p>
    <h1 class="card__name gold-text">MARISELA VONDRAKE</h1>
    <div class="contact">
      <div class="contact__row">
        <div>
          <p class="contact__phone gold-text">555 218 9031</p>
          <p class="contact__email gold-text">mariselavondrake@mailbox.com</p>
        </div>
        <div class="contact__icons">
          <svg width="16" height="16" viewBox="0 0 24 24" aria-label="Phone"><path fill="url(#goldStroke)" d="M6.6 10.8a15 15 0 0 0 6.6 6.6l2.2-2.2c.3-.3.7-.4 1-.2 1.1.4 2.3.6 3.6.6.6 0 1 .4 1 1V20c0 .6-.4 1-1 1A17 17 0 0 1 3 4c0-.6.4-1 1-1h3.5c.6 0 1 .4 1 1 0 1.3.2 2.5.6 3.6.1.3 0 .7-.2 1z"/></svg>
          <svg width="16" height="16" viewBox="0 0 24 24" aria-label="Email"><path fill="url(#goldStroke)" d="M2 5h20v14H2zm2 2v.5l8 5 8-5V7l-8 5z"/></svg>
        </div>
      </div>
      <p class="contact__web gold-text">www.VondrakeSkin.com</p>
      <span class="contact__rule"></span>
    </div>
  </section>

  <section class="card card--light">
    <svg class="frame" viewBox="0 0 340 310" aria-hidden="true">
      <path d="M340,108 V0 H0 V310 H340 V188" fill="none" stroke="url(#goldStroke)" stroke-width="2"/>
    </svg>
    <p class="card__title gold-text">Skin care expert</p>
    <h1 class="card__name gold-text">MARISELA VONDRAKE</h1>
    <div class="contact">
      <div class="contact__row">
        <div>
          <p class="contact__phone gold-text">555 218 9031</p>
          <p class="contact__email gold-text">mariselavondrake@mailbox.com</p>
        </div>
        <div class="contact__icons">
          <svg width="16" height="16" viewBox="0 0 24 24" aria-label="Phone"><path fill="url(#goldStroke)" d="M6.6 10.8a15 15 0 0 0 6.6 6.6l2.2-2.2c.3-.3.7-.4 1-.2 1.1.4 2.3.6 3.6.6.6 0 1 .4 1 1V20c0 .6-.4 1-1 1A17 17 0 0 1 3 4c0-.6.4-1 1-1h3.5c.6 0 1 .4 1 1 0 1.3.2 2.5.6 3.6.1.3 0 .7-.2 1z"/></svg>
          <svg width="16" height="16" viewBox="0 0 24 24" aria-label="Email"><path fill="url(#goldStroke)" d="M2 5h20v14H2zm2 2v.5l8 5 8-5V7l-8 5z"/></svg>
        </div>
      </div>
      <p class="contact__web gold-text">www.VondrakeSkin.com</p>
      <span class="contact__rule"></span>
    </div>
  </section>
</main>
</body>
</html>
```